Penny Harvest

Logo and general packaging design for premium quality, price conscious super foods.

Initial product portfolio includes:

Organic Raw Chia Seeds - Resealable plastic bags with 3 x 5 label.
Organic Cold Pressed Coconut Oil (plastic jar) - 2.5 x 6.5 label

The design should be transferable to additional products.

Project requirements:

The design should be simple and the core trade dress should be no more than 2 or 3 colors. The logo should reproduce well in black/1 color.

The idea of this design is to convey quality and simplicity, like a "no frills", premium quality brand.

Deliverable: fully editable (text and illustration):

Logo.

Basic Jar label design.

Basic Bag label design.

Target Market(s)

Educated women aged 22-45

Industry/Entity Type

Plastic

Requirements
Must have
• Clear, simple logo, delivered in vector form, 1 color/black.
• Use of logo on 1 jar label and 1 bag label, each with product name and space for required and optional marketing content.
Nice to have
• Additional iterations of the design to demonstrate your concept of how we will visually vary additional items in jars and bags.
• i.e. What an additional product in a bag would look like for purposes of brand consistency and product differentiation on shelf or online in e-store.
Should not have
• overly detailed graphics that don't scale well and/or may be hard to read or understand. 4 color design elements (except to simiulate how the product may look through the clear jar or bag or how the product may be placed in a simulated surrounding or ad.

```html
<!DOCTYPE html>
<html lang="en">
<head>
<meta charset="utf-8">
<title>Penny Harvest – Organic Raw Chia Seeds Label</title>
<link rel="stylesheet" href="https://fonts.googleapis.com/css2?family=Cinzel:wght@600&family=Montserrat:wght@500;600;700;800&display=swap">
<style>
  :root {
    --label-green: #8f9d5f;
    --ink-white: #ffffff;
    --plant-pale: #c9cfae;
    --badge-green: #7f8f4e;
    --placeholder-grey: #9a9a9a;
  }
  * { margin: 0; padding: 0; box-sizing: border-box; }
  html, body { width: 1200px; height: 721px; overflow: hidden; }
  body { background: var(--label-green); font-family: "Montserrat", Arial, sans-serif; color: var(--ink-white); }

  .label { position: relative; width: 1200px; height: 721px; background: var(--label-green); overflow: hidden; }

  .plant-art {
    position: absolute; left: 100px; top: 0; width: 300px; height: 721px;
    background: linear-gradient(180deg, rgba(201,207,174,0.55) 0%, rgba(201,207,174,0.35) 60%, rgba(201,207,174,0.15) 100%);
    border-radius: 120px 120px 0 0;
  }

  .side-info {
    position: absolute; writing-mode: vertical-rl;
    font-size: 16px; font-weight: 500; line-height: 32px; color: var(--ink-white);
  }
  .side-info--dates { left: 12px; top: 178px; }
  .side-info--marketer { left: 12px; top: 438px; }

  .brand { position: absolute; left: 0; width: 1200px; top: 86px; text-align: center; }
  .brand-mark { display: block; margin: 0 auto 18px; }
  .brand-name { font-family: "Cinzel", Georgia, serif; font-weight: 600; font-size: 40px; letter-spacing: 3px; }

  .natural-seal {
    position: absolute; left: 926px; top: 160px; width: 120px; height: 120px; border-radius: 50%;
    background: var(--ink-white); color: var(--badge-green);
    display: flex; flex-direction: column; align-items: center; justify-content: center;
    font-weight: 700; line-height: 1;
  }
  .natural-seal__pct { font-size: 29px; }
  .natural-seal__word { font-size: 24px; margin-top: 2px; }

  .product-title { position: absolute; left: 0; width: 1210px; text-align: center; font-weight: 800; line-height: 1; }
  .product-title--main { top: 282px; font-size: 128px; letter-spacing: 2px; }
  .product-title--sub { top: 404px; font-size: 68px; font-weight: 700; letter-spacing: 1px; }

  .divider { position: absolute; left: 550px; top: 495px; width: 112px; height: 2px; background: var(--ink-white); }

  .benefits { position: absolute; left: 0; width: 1212px; top: 522px; text-align: center; font-size: 22px; font-weight: 600; letter-spacing: 1px; }

  .net-weight { position: absolute; left: 0; width: 1180px; top: 626px; text-align: center; font-size: 16px; font-weight: 600; line-height: 23px; }

  .barcode-space {
    position: absolute; left: 1092px; top: 479px; width: 90px; height: 242px;
    background: var(--ink-white);
    display: flex; align-items: center; justify-content: center;
  }
  .barcode-space__text {
    writing-mode: vertical-rl; color: var(--placeholder-grey);
    font-size: 16px; font-weight: 500; letter-spacing: 1px;
  }
</style>
</head>
<body>
<main class="label">
  <div class="plant-art" role="img" aria-label="Faint illustration of flowering chia plant stems rising from the bottom edge"></div>

  <p class="side-info side-info--dates">Date of packing:<br>Expiry date:</p>
  <p class="side-info side-info--marketer">Marketed by: Penny Harvest<br>abc, 5678, RVT, 40517.</p>

  <header class="brand">
    <svg class="brand-mark" width="40" height="40" viewBox="0 0 40 40" aria-hidden="true">
      <circle cx="20" cy="20" r="17" fill="none" stroke="#ffffff" stroke-width="3"/>
    </svg>
    <div class="brand-name">PENNY HARVEST</div>
  </header>

  <div class="natural-seal">
    <span class="natural-seal__pct">100%</span>
    <span class="natural-seal__word">natural</span>
  </div>

  <h1 class="product-title product-title--main">ORGANIC</h1>
  <h2 class="product-title product-title--sub">RAW CHIA SEEDS</h2>

  <div class="divider" aria-hidden="true"></div>

  <p class="benefits">ANTIOXIDANTS &nbsp;|&nbsp; CALCIUM &nbsp;|&nbsp; OMEGA FATTY ACIDS</p>

  <p class="net-weight">Net Weight<br>100gms</p>

  <div class="barcode-space"><span class="barcode-space__text">BARCODE</span></div>
</main>
</body>
</html>
```